Bold Website Design for Fitness Trainer - No Coding

We are in need of a bold and unique website design for a personal fitness training company, www.TessaRowle.com. We need DESIGN ONLY for three pages. These will be a homepage, a lead capture page, and one internal page with a sidebar. The design will be used for coding a wordpress theme, if that matters for the designer.

Tessa Rowle Fitness Training
2718 E 57th St #193
Austin, TX 78705
512-460-7198
http://www.tessarowle.com

Target Market(s)

18-45 year old male and females making 80k+ a year and looking to get stronger and in shape.

Industry/Entity Type

Fitness

Number of Pages Required

3 page

Font styles to use
Sans Serif

Requirements
Must have
• See attached design specs file.
Nice to have
Should not have
• Boxed layout.
• Dark Background.

```html
<!DOCTYPE html>
<html lang="en">
<head>
<meta charset="utf-8">
<title>Tessa Rowle Fitness Training</title>
<link href="https://fonts.googleapis.com/css2?family=Fjalla+One&family=Open+Sans:ital,wght@0,400;0,600;0,700;1,400&family=Noto+Serif:ital@1&display=swap" rel="stylesheet">
<style>
:root{
  --cyan:#15b4e8;
  --pink:#ec2c8c;
  --yellow:#f6d90f;
  --dark:#2b2b2b;
  --ink:#333;
  --muted:#666;
  --light:#efefef;
  --white:#fff;
}
*{box-sizing:border-box;margin:0;padding:0}
html,body{width:1200px;height:3697px;overflow:hidden}
body{font-family:"Open Sans",Arial,sans-serif;color:var(--ink);background:var(--white);position:relative}
.display{font-family:"Fjalla One","Arial Narrow",sans-serif;font-weight:400}
section,header,footer{position:relative;width:1200px}
.abs{position:absolute}
.btn{display:inline-flex;align-items:center;justify-content:center;gap:10px;color:#fff;text-decoration:none}
.btn-pink{background:var(--pink)}
.btn-dark{background:#222;font-size:15px;letter-spacing:1px;width:92px;height:28px}

/* top bar */
.topbar{height:47px;background:var(--dark);color:#ddd;font-size:15px}
.topbar .social{left:84px;top:12px;display:flex;gap:10px}
.topbar .social span{width:22px;height:22px;background:#999;display:block;border-radius:2px}
.topbar .info{right:84px;top:13px;display:flex;gap:34px;align-items:center}
.topbar .info span{display:flex;align-items:center;gap:7px}

/* header */
.brand{height:181px;background:#fff;border-bottom:3px solid #cfcfcf}
.logo{left:360px;top:28px;display:flex;align-items:center;gap:16px}
.logo .mark{width:110px;height:110px;border-radius:50%;background:var(--cyan)}
.logo .name{font-family:"Fjalla One",sans-serif;font-size:62px;color:var(--dark);line-height:1}
.logo .sub{font-size:18px;font-weight:700;letter-spacing:2px;color:var(--dark)}
.nav{height:54px;background:var(--yellow);display:flex;justify-content:center;gap:52px;align-items:center;font-size:19px;color:#222}
.nav a{color:#222;text-decoration:none;position:relative}
.nav a.active{color:#c01874}
.nav a.active::after{content:"";position:absolute;left:0;right:0;bottom:-16px;height:4px;background:var(--pink)}

/* hero */
.hero{height:525px;background:linear-gradient(100deg,#1d1d1d 0%,#5a5a5a 45%,#8b8b8b 70%,#3a3a3a 100%)}
.hero .copy{left:195px;top:200px}
.hero h1{font-size:66px;color:var(--cyan);line-height:1}
.hero h2{font-size:40px;color:#fff;margin-top:14px}
.hero p{font-size:30px;color:#fff;margin-top:8px}
.dots{display:flex;gap:8px}
.dots i{width:16px;height:16px;border-radius:50%;background:var(--yellow);border:2px solid #222;display:block}
.hero .dots{left:560px;top:476px}

/* free session band */
.free{height:319px;background:var(--cyan);border-top:10px solid var(--yellow);text-align:center;color:#fff}
.free h2{font-size:46px;padding-top:36px}
.free p{font-size:20px;line-height:1.45;margin:14px auto 0;width:820px}
.free .btn{position:absolute;left:478px;top:224px;width:220px;height:48px;font-size:26px;font-family:"Fjalla One",sans-serif}
.free svg{position:absolute;left:378px;top:182px}

/* welcome */
.welcome{height:225px;text-align:center;background:linear-gradient(#fff 65%,#e9e9e9)}
.welcome h2{font-family:"Fjalla One",sans-serif;font-size:40px;color:#222;padding-top:24px}
.welcome p{font-size:14px;line-height:1.55;width:1040px;margin:14px auto 0;color:#444}
.welcome .btn{width:150px;height:34px;font-size:18px;letter-spacing:2px;margin-top:14px}

/* services */
.services{height:397px;background:linear-gradient(#f4f4f4,#fff)}
.service{width:296px;top:44px;text-align:center}
.service h3{font-family:"Fjalla One",sans-serif;font-size:27px;color:#222;font-weight:400}
.service .photo{width:296px;height:155px;margin-top:20px;background:linear-gradient(135deg,#3d3d3d,#8a8a8a)}
.service p{font-size:14px;line-height:1.4;margin:10px 0 8px;color:#444}
.service .badge{position:absolute;left:50%;transform:translateX(-50%);top:80px;color:#fff;font-family:"Fjalla One",sans-serif;font-size:30px;line-height:1.3}
.service .badge b{background:var(--pink);font-weight:400;font-size:20px;padding:2px 8px;margin-left:6px}

/* testimonial */
.testimonial{height:286px;margin-top:33px;background:linear-gradient(90deg,#dcdcdc,#f3f3f3 50%,#cfcfcf);border-top:1px solid #ddd}
.testimonial h3{left:0;right:0;top:34px;text-align:center;font-family:"Fjalla One",sans-serif;font-size:28px;color:#333;font-weight:400}
.testimonial .avatar{left:136px;top:90px;width:134px;height:134px;border-radius:50%;background:var(--cyan);border:6px solid var(--yellow)}
.testimonial blockquote{left:330px;top:96px;width:760px;font-family:"Noto Serif",serif;font-style:italic;font-size:26px;line-height:1.3;color:#333}
.testimonial cite{display:block;font-size:20px;color:var(--pink);margin-top:8px}
.testimonial .dots{left:560px;top:242px}

/* social feeds */
.buzz{height:555px;text-align:center}
.buzz h2{font-family:"Fjalla One",sans-serif;font-size:36px;color:#222;padding-top:22px;font-weight:400}
.buzz .lead{font-size:20px;color:#444;margin-top:4px}
.feed{border:1px solid #ccc;background:#fff;text-align:left}
.feed.photos{left:192px;top:125px;width:420px;height:396px;padding:16px 22px}
.feed.photos h4{font-size:17px;font-weight:400;color:#444}
.feed.photos small{font-size:12px;color:#888}
.feed .grid{display:grid;gap:6px;margin-top:14px}
.feed.photos .grid{grid-template-columns:repeat(4,1fr)}
.feed.photos .grid span{height:64px;background:linear-gradient(135deg,#555,#a88)}
.feed.page{left:640px;top:125px;width:358px;height:396px;padding:14px 18px}
.feed.page .grid{grid-template-columns:repeat(3,1fr)}
.feed.page .grid span{height:76px;background:#ddd}
.feed .row{font-size:12px;color:#777;margin-top:8px}

/* blog */
.blog{height:370px;background:#ececec;margin-top:17px}
.blog h2{text-align:center;font-family:"Fjalla One",sans-serif;font-size:32px;color:#222;padding-top:32px;font-weight:400}
.post{top:118px;width:504px;display:flex;gap:18px}
.post .thumb{width:156px;height:150px;background:linear-gradient(135deg,#1ca4d8,#444)}
.post h4{font-family:"Fjalla One",sans-serif;font-weight:400;font-size:17px;color:#222}
.post .meta{font-size:12px;color:#666;margin:6px 0}
.post p{font-size:13px;line-height:1.35;color:#555}
.post .foot{font-size:12px;color:#555;text-align:right;margin-top:14px;border-top:1px solid #ccc;padding-top:4px}

/* call to action */
.cta{height:252px;margin-top:33px;background:linear-gradient(100deg,#1b1b1b,#555 50%,#222);border-top:10px solid var(--yellow);text-align:center;color:#fff}
.cta h2{font-size:46px;padding-top:34px;line-height:1.1}
.cta h3{font-size:34px;font-weight:400;font-family:"Fjalla One",sans-serif}
.cta .btn{width:220px;height:48px;font-size:26px;font-family:"Fjalla One",sans-serif;margin-top:14px}

/* footer */
.site-footer{height:279px;margin-top:17px}
.site-footer h4{font-family:"Fjalla One",sans-serif;font-size:26px;color:#222;font-weight:400}
.col{top:40px}
.col p,.col li{font-size:14px;line-height:1.5;color:#444;list-style:none}
.contact{left:110px}
.contact .flogo{width:110px;height:110px;border-radius:50%;background:var(--cyan);margin-top:20px;float:left;margin-right:16px}
.contact .info{margin-top:20px;float:left}
.contact .info strong{color:var(--pink);font-weight:700;font-size:14px}
.resources{left:528px}
.resources ul{margin-top:20px}
.social-col{left:752px}
.social-col ul{display:grid;grid-template-columns:repeat(3,auto);gap:6px 22px;margin-top:20px}
.social-col li{display:flex;align-items:center;gap:6px}
.social-col li i{width:14px;height:14px;background:#555;display:block}
.copyright{position:absolute;left:0;top:3623px;width:1200px;height:74px;background:var(--cyan);color:#fff;text-align:center;font-size:14px;line-height:74px}
</style>
</head>
<body>

<header class="topbar">
  <div class="abs social"><span></span><span></span><span></span><span></span><span></span></div>
  <div class="abs info">
    <span><svg width="14" height="14" viewBox="0 0 24 24"><path fill="#ddd" d="M6 2l4 4-2 3c1 3 4 6 7 7l3-2 4 4-3 4C10 21 3 14 2 5z"/></svg>(512) 460-7198</span>
    <span><svg width="12" height="16" viewBox="0 0 12 16"><path fill="#ddd" d="M6 0a6 6 0 0 0-6 6c0 4 6 10 6 10s6-6 6-10a6 6 0 0 0-6-6zm0 8a2 2 0 1 1 0-4 2 2 0 0 1 0 4z"/></svg>LOCATIONS</span>
    <span><svg width="14" height="14" viewBox="0 0 14 14"><rect x="1" y="2" width="12" height="11" fill="none" stroke="#ddd" stroke-width="1.5"/><line x1="1" y1="5" x2="13" y2="5" stroke="#ddd" stroke-width="1.5"/></svg>TRAINING CALENDAR</span>
  </div>
</header>

<div class="brand">
  <div class="abs logo">
    <span class="mark"></span>
    <div><div class="name">Tessa Rowle</div><div class="sub">FITNESS TRAINING</div></div>
  </div>
</div>

<nav class="nav">
  <a class="active">Home</a><a>Programs</a><a>Meet Your Trainer</a><a>Blog</a><a>Contact Me</a><a>Free Session</a>
</nav>

<section class="hero" role="img" aria-label="Black and white photo of a trainer in a gym beside a weight rack">
  <div class="abs copy">
    <h1 class="display">Tessa Rowle</h1>
    <h2 class="display">Personal Trainer and Workouts custom tailored to you</h2>
    <p>Lose Weight Feel Sexy &amp; be Amazing</p>
  </div>
  <div class="abs dots"><i></i><i></i><i></i><i></i><i></i></div>
</section>

<section class="free">
  <h2 class="display">Get Started Today – Your First Sessions is Free!</h2>
  <p>Come and see what’s all about. Contact us to schedule a time to come by and see our facility, learn more about us, and even get a 1-on-1 training session!</p>
  <svg width="100" height="80" viewBox="0 0 100 80"><path d="M10 5 C0 40 30 62 90 60" fill="none" stroke="#1b1b1b" stroke-width="3"/><path d="M80 50 L92 60 L80 70" fill="none" stroke="#1b1b1b" stroke-width="3"/></svg>
  <a class="btn btn-pink">Sign up now <svg width="22" height="22" viewBox="0 0 22 22"><circle cx="11" cy="11" r="9" fill="none" stroke="#fff" stroke-width="2"/><path d="M7 11h8M12 7l4 4-4 4" fill="none" stroke="#fff" stroke-width="2"/></svg></a>
</section>

<section class="welcome">
  <h2>Welcome to our website</h2>
  <p>Lorem ipsum dolor sit amet, consectetur adipiscing elit. Aliquam ultrices eros a ex bibendum feugiat. Etiam lorem dui, rhoncus at congue vel, vehicula in ex. Nullam nunc massa, elementum ac risus aliquet, sodales tristique mauris. Donec ultricies purus in tincidunt mollis. Ut ultrices mollis iaculis. Mauris libero lacus, eleifend sed imperdiet sit amet, tempus at ipsum. In scelerisque nisi neque, id interdum magna luctus in.</p>
  <a class="btn btn-pink">MORE</a>
</section>

<section class="services">
  <div class="abs service" style="left:80px">
    <h3>1-on-1 Personal Training</h3>
    <div class="photo" role="img" aria-label="Photo of a trainer coaching a client at a bench press"></div>
    <p>Lorem ipsum dolor sit amet, consectetur adipiscing elit. Aliquam ultrices eros a ex bibendum feugiat.</p>
    <a class="btn btn-dark">MORE</a>
  </div>
  <div class="abs service" style="left:452px">
    <h3>Online Coaching</h3>
    <div class="photo" role="img" aria-label="Dark photo of a coach in a gym"></div>
    <div class="badge">FREE<b>5 Days</b><br>COACH PREVIEW</div>
    <p>Lorem ipsum dolor sit amet, consectetur adipiscing elit. Aliquam ultrices eros a ex bibendum feugiat.</p>
    <a class="btn btn-dark">MORE</a>
  </div>
  <div class="abs service" style="left:824px">
    <h3>Strength Programming</h3>
    <div class="photo" role="img" aria-label="Photo of a client lifting with a spotter"></div>
    <p>Lorem ipsum dolor sit amet, consectetur adipiscing elit. Aliquam ultrices eros a ex bibendum feugiat.</p>
    <a class="btn btn-dark">MORE</a>
  </div>
</section>

<section class="testimonial" role="img" aria-label="Faded gym photo behind a customer testimonial">
  <h3 class="abs">What Our Community is saying..</h3>
  <div class="abs avatar" role="img" aria-label="Customer portrait"></div>
  <blockquote class="abs">“Lorem ipsum dolor sit amet, consectetur adipiscing elit. Curabitur varius neque ac leo semper, ut tempus quam fringilla.”<cite>Dana Merrick, Customer</cite></blockquote>
  <div class="abs dots"><i></i><i></i><i></i><i></i></div>
</section>

<section class="buzz">
  <h2>All the Buzz..</h2>
  <p class="lead">Find out what’s happening with Tessa Rowle around the Internet.</p>
  <div class="abs feed photos">
    <h4>PHOTO FEED</h4>
    <small>by @tessarowle · 35 photos · 4,330 followers</small>
    <div class="grid" role="img" aria-label="Grid of recent training photos">
      <span></span><span></span><span></span><span></span><span></span><span></span><span></span><span></span><span></span><span></span><span></span><span></span><span></span><span></span><span></span><span></span>
    </div>
    <div class="row" style="text-align:right">Powered by FEEDBOX</div>
  </div>
  <div class="abs feed page">
    <div style="display:flex;gap:10px;align-items:center"><span style="width:40px;height:40px;background:var(--cyan);display:block"></span><div style="font-size:13px"><b>Tessa Rowle Web</b> on Social Page<br><span style="color:#888">Like · You like this.</span></div></div>
    <div class="row">1076 people like Tessa Rowle</div>
    <div class="grid" role="img" aria-label="Follower thumbnails">
      <span></span><span></span><span></span><span></span><span></span><span></span><span></span><span></span><span></span><span></span><span></span><span></span>
    </div>
    <div class="row">Social page plugin</div>
  </div>
</section>

<section class="blog">
  <h2>Read Our Blog</h2>
  <article class="abs post" style="left:84px">
    <div class="thumb" role="img" aria-label="Workout photos of two athletes"></div>
    <div>
      <h4>Chest, Shoulders, Triceps and Back</h4>
      <div class="meta">September 7, 2013 · Workout Training Log</div>
      <p>Lorem ipsum dolor sit amet, consectetur adipiscing elit. Suspendisse a odio luctus, blandit dui quis, tempor purus. Ut risus ligula, pulvinar ut vestibulum in, semper a velit.</p>
      <div class="foot">2 comments · Read more</div>
    </div>
  </article>
  <article class="abs post" style="left:640px">
    <div class="thumb" role="img" aria-label="Workout photos of two athletes"></div>
    <div>
      <h4>Chest, Shoulders, Triceps and Back</h4>
      <div class="meta">September 7, 2013 · Workout Training Log</div>
      <p>Lorem ipsum dolor sit amet, consectetur adipiscing elit. Suspendisse a odio luctus, blandit dui quis, tempor purus. Ut risus ligula, pulvinar ut vestibulum in, semper a velit.</p>
      <div class="foot">2 comments · Read more</div>
    </div>
  </article>
</section>

<section class="cta" role="img" aria-label="Dark gym floor photo behind the free trial call to action">
  <h2 class="display">What are You Waiting For</h2>
  <h3>Schedule Your Free Trial!</h3>
  <a class="btn btn-pink">Sign up now <svg width="22" height="22" viewBox="0 0 22 22"><circle cx="11" cy="11" r="9" fill="none" stroke="#fff" stroke-width="2"/><path d="M7 11h8M12 7l4 4-4 4" fill="none" stroke="#fff" stroke-width="2"/></svg></a>
</section>

<footer class="site-footer">
  <div class="abs col contact">
    <h4>Contact info</h4>
    <span class="flogo"></span>
    <div class="info"><p><strong>Tessa Rowle Fitness Training</strong><br>2718 E 57th St #193<br>Austin, TX 78705<br>(512) 460-7198</p></div>
  </div>
  <div class="abs col resources">
    <h4>Resources</h4>
    <ul><li>Lorem ipsum dolor</li><li>sit amet consectetur</li><li>Adipiscing elit</li><li>Suspendisse a</li><li>Odio luctus</li></ul>
  </div>
  <div class="abs col social-col">
    <h4>Social Media</h4>
    <ul><li><i></i>Social Page</li><li><i></i>Circle Share</li><li><i></i>Video Channel</li><li><i></i>Pin Board</li><li><i></i>Photo Feed</li></ul>
  </div>
</footer>

<div class="copyright">Copyright © 2015 - Jamie Ortiz</div>

</body>
</html>
```